40-year-old commercial construction firm :: Business Card Revamp

We are a 40 year-old, private general construction company based in Dallas, Texas, and we are considering updating our business cards, which could lead to a larger "brand refresh" campaign.

We work in a competitive environment, selling to business owners and executives making large scale purchasing decisions on behalf of their firms. A majority of our business is repeat business, with a long sales-cycle; while business can be difficult to identify and land, the effort is often rewarded with multiple projects.

We are open to a logo "refresh" as well as designs that incorporate the existing logo.

Target Market(s)

B2B selling to business owners/executives/end users who make facility decisions for their firms.

Industry/Entity Type

Construction Company

Contact Information for Business Card

Refresh from the example provided

Logo Text

Harkel Building Company :: See card example

Font styles to use
Other font styles liked:
• See sample card :: Designers to choose

Colors

Designer to choose colors to be used in the design.

Requirements
Must have
• Design should convey:
• Confidence
• Competence
• Capability
• Stability
• Tagline: Genuine Relationships :: Superior Services :: Environmentally Aware
Nice to have
• A solid design that is transferable from print to online.
• Note that we are also considering a painted-edge printing / card design
Should not have
• Too much color or whimsy. Our clients tend to be the serious type, and we work hard to present a serious, professional presence in the marketplace.

```html
<!DOCTYPE html>
<html lang="en">
<head>
<meta charset="utf-8">
<title>Harkel Building Company – Business Card</title>
<link href="https://fonts.googleapis.com/css2?family=Open+Sans:wght@400&family=Work+Sans:wght@400;500&display=swap" rel="stylesheet">
<style>
  :root {
    --backdrop: #1b1b1c;
    --card: #121213;
    --card-edge: #1a1a1b;
    --silver: #e6e6e6;
    --silver-dim: #bdbdbd;
    --tagline: #8f8f8f;
    --logo-dim: #3c3c3d;
    --rule: #8a8a8a;
  }
  * { margin: 0; padding: 0; box-sizing: border-box; }
  html, body {
    width: 1200px; height: 900px; overflow: hidden;
    background: var(--backdrop);
  }
  .canvas {
    position: relative; width: 1200px; height: 900px;
    display: flex; flex-direction: column; align-items: center; justify-content: center; gap: 36px;
  }
  .card {
    position: relative; width: 630px; height: 360px;
    background: linear-gradient(135deg, var(--card-edge), var(--card) 60%);
    box-shadow: 0 10px 30px rgba(0,0,0,.55);
  }
  .wordmark {
    font-family: "Open Sans", sans-serif; font-weight: 400;
    display: flex; align-items: center; gap: 16px;
  }
  .wordmark__dot {
    width: 58px; height: 58px; border-radius: 50%;
    border: 2px solid currentColor;
  }
  .wordmark__name { font-size: 52px; line-height: 1; letter-spacing: -0.5px; }
  .wordmark__sub { font-size: 15px; letter-spacing: 1.2px; margin-top: 4px; white-space: nowrap; }

  .card--front .wordmark {
    position: absolute; left: 50%; top: 50%; transform: translate(-50%, -50%);
    color: var(--silver);
  }
  .tagline {
    position: absolute; left: 0; right: 0; bottom: 34px;
    text-align: center;
    font-family: "Work Sans", sans-serif; font-weight: 400;
    font-size: 11px; letter-spacing: 1.4px; text-transform: uppercase;
    color: var(--tagline); white-space: nowrap;
  }

  .card--back .wordmark {
    position: absolute; left: 40px; top: 50%; transform: translateY(-50%);
    color: var(--logo-dim);
  }
  .card--back .wordmark__name { font-size: 44px; }
  .card--back .wordmark__dot { width: 50px; height: 50px; }
  .card--back .wordmark__sub { font-size: 13px; }

  .divider {
    position: absolute; left: 352px; top: 62px; width: 1px; height: 236px;
    background: var(--rule);
  }
  .contact {
    position: absolute; left: 376px; top: 76px; right: 20px;
    font-family: "Work Sans", sans-serif; color: var(--silver-dim);
  }
  .contact__name {
    font-size: 23px; font-weight: 500; letter-spacing: 2.2px; color: var(--silver);
    white-space: nowrap;
  }
  .contact__role { font-size: 13px; margin-bottom: 12px; }
  .contact__address { font-size: 14px; line-height: 1.35; margin-bottom: 10px; }
  .contact__list { list-style: none; font-size: 15px; line-height: 1.4; }
  .contact__list li { display: flex; align-items: center; gap: 10px; white-space: nowrap; }
  .contact__list svg { width: 11px; height: 11px; flex: none; }
</style>
</head>
<body>
<main class="canvas">
  <section class="card card--front" aria-label="Card front">
    <div class="wordmark">
      <span class="wordmark__dot"></span>
      <div>
        <div class="wordmark__name">Harkel</div>
        <div class="wordmark__sub">BUILDING COMPANY, LTD</div>
      </div>
    </div>
    <p class="tagline">Genuine Relationships :: Superior Services :: Environmentally Aware</p>
  </section>

  <section class="card card--back" aria-label="Card back">
    <div class="wordmark">
      <span class="wordmark__dot"></span>
      <div>
        <div class="wordmark__name">Harkel</div>
        <div class="wordmark__sub">BUILDING COMPANY, LTD</div>
      </div>
    </div>
    <div class="divider"></div>
    <div class="contact">
      <div class="contact__name">MARCUS DALTON</div>
      <div class="contact__role">Director</div>
      <div class="contact__address">48 Meridian Park Drive,<br>Suite 210, Ridgefield, TX</div>
      <ul class="contact__list">
        <li>
          <svg viewBox="0 0 12 12" fill="none" stroke="currentColor" stroke-width="1.2"><rect x="3" y="0.8" width="6" height="10.4" rx="1"/><line x1="5" y1="9.4" x2="7" y2="9.4"/></svg>
          +1 555 014 2870
        </li>
        <li>
          <svg viewBox="0 0 12 12" fill="currentColor"><path d="M2.4 1l2 .2 1 2.6-1.3 1a6 6 0 0 0 3.1 3.1l1-1.3 2.6 1 .2 2c-.6.9-1.6 1.3-2.6 1.1C4.6 10.1 1.9 7.4 1.3 3.6 1.1 2.6 1.5 1.6 2.4 1z"/></svg>
          +1 555 014 2871
        </li>
        <li>
          <svg viewBox="0 0 12 12" fill="none" stroke="currentColor" stroke-width="1.1"><rect x="0.8" y="2.2" width="10.4" height="7.6"/><polyline points="0.8,2.4 6,6.6 11.2,2.4"/></svg>
          info@harkelbuilding.com
        </li>
        <li>
          <svg viewBox="0 0 12 12" fill="none" stroke="currentColor" stroke-width="1"><circle cx="6" cy="6" r="5"/><ellipse cx="6" cy="6" rx="2.2" ry="5"/><line x1="1" y1="6" x2="11" y2="6"/></svg>
          www.harkelbuilding.com
        </li>
      </ul>
    </div>
  </section>
</main>
</body>
</html>
```